Country Duo act needs single artwork

We need artwork for our latest single for tunorra and other music streaming sites. The design can include the pictures in the attached files that we uploaded but we are also open to designs that also don't include them. It should be easy to read the song title
"Rain Won't Wait" and our band name Orchard 19 - this track is our actual story. Must be at least 640 x 640 pixels to be acceptable to tunorra. We have also included a copy of the track for inspiration.
Check us out on tunorra to see other artwork -> https://play.tunorra.net/artist/8QkTbnR4wXe71PuzMdGhVc?si=Hq3LmPa-Tb9Wn2KcXoRvEd

Target Market(s)

Country music fans

Industry/Entity Type

Music

Font styles to use
Decorative

Colors

Designer to choose colors to be used in the design.

Requirements
Must have
• Name of song Title and band name
Nice to have
• Vibe that matches the song / one of our pictures included
Should not have
• any other text

```html
<!DOCTYPE html>
<html lang="en">
<head>
<meta charset="utf-8">
<title>Rain Won't Wait – Orchard 19</title>
<link rel="stylesheet" href="https://fonts.googleapis.com/css2?family=Bebas+Neue&display=swap">
<style>
  :root {
    --canvas-bg: #000000;
    --cover-red: #f20804;
    --cover-edge: #8a0904;
    --rain-streak: #8a0904;
    --ink: #000000;
  }
  html, body {
    margin: 0;
    padding: 0;
    width: 1200px;
    height: 1000px;
    overflow: hidden;
    background: var(--canvas-bg);
  }
  .artwork {
    display: block;
    width: 1200px;
    height: 1000px;
  }
  .cover-edge-stop { stop-color: var(--cover-edge); }
  .cover-red-stop { stop-color: var(--cover-red); }
  .rain-streak {
    stroke: var(--rain-streak);
    stroke-linecap: round;
    fill: none;
  }
  .title-line,
  .band-name {
    font-family: "Bebas Neue", "Oswald", sans-serif;
    fill: var(--ink);
  }
</style>
</head>
<body>
<svg class="artwork" viewBox="0 0 1200 1000" xmlns="http://www.w3.org/2000/svg">
  <defs>
    <clipPath id="cover-clip">
      <rect x="312" y="213" width="575" height="576"/>
    </clipPath>
    <radialGradient id="cover-glow" cx="640" cy="520" r="440" gradientUnits="userSpaceOnUse">
      <stop offset="0" class="cover-red-stop"/>
      <stop offset="0.62" class="cover-red-stop"/>
      <stop offset="1" class="cover-edge-stop"/>
    </radialGradient>
  </defs>

  <g class="cover" clip-path="url(#cover-clip)">
    <rect class="cover-base" x="312" y="213" width="575" height="576" fill="url(#cover-glow)"/>
    <g class="rain-field" opacity="0.85">
      <line class="rain-streak" x1="352" y1="236" x2="332" y2="316" stroke-width="4"/>
      <line class="rain-streak" x1="418" y1="262" x2="402" y2="326" stroke-width="3"/>
      <line class="rain-streak" x1="486" y1="228" x2="466" y2="308" stroke-width="4"/>
      <line class="rain-streak" x1="380" y1="352" x2="360" y2="432" stroke-width="4"/>
      <line class="rain-streak" x1="456" y1="376" x2="440" y2="440" stroke-width="3"/>
      <line class="rain-streak" x1="515" y1="330" x2="499" y2="394" stroke-width="3"/>
      <line class="rain-streak" x1="340" y1="470" x2="324" y2="534" stroke-width="3"/>
      <line class="rain-streak" x1="420" y1="482" x2="400" y2="562" stroke-width="4"/>
      <line class="rain-streak" x1="500" y1="456" x2="484" y2="520" stroke-width="3"/>
      <line class="rain-streak" x1="372" y1="586" x2="352" y2="666" stroke-width="4"/>
      <line class="rain-streak" x1="460" y1="600" x2="444" y2="664" stroke-width="3"/>
      <line class="rain-streak" x1="516" y1="566" x2="500" y2="630" stroke-width="3"/>
      <line class="rain-streak" x1="336" y1="700" x2="320" y2="764" stroke-width="3"/>
      <line class="rain-streak" x1="414" y1="702" x2="394" y2="782" stroke-width="4"/>
      <line class="rain-streak" x1="496" y1="690" x2="480" y2="754" stroke-width="3"/>
    </g>
  </g>

  <g class="single-title" aria-label="Rain Won't Wait">
    <text class="title-line" x="538" y="462" font-size="231" textLength="312" lengthAdjust="spacingAndGlyphs">RAIN</text>
    <text class="title-line" x="538" y="565" font-size="136" textLength="312" lengthAdjust="spacingAndGlyphs">WON'T</text>
    <text class="title-line" x="538" y="720" font-size="211" textLength="312" lengthAdjust="spacingAndGlyphs">WAIT</text>
  </g>
  <text class="band-name" x="540" y="772" font-size="49" textLength="305" lengthAdjust="spacing">ORCHARD 19</text>
</svg>
</body>
</html>
```